Investment company needing business card

We are wanting a business card which looks sharp and easy on the eye. We are thinking of having a business card with the logo embossed on it, to really make it stand out. We will only have a small amount of information of the business card, person's name, position, email address and phone number

Contact Information for Business Card

Danica Pruett
Executive Assistant
+64 21 547 3162
danicap@harwellcapital.co.nz

Requirements
Must have
• Embossed logo
Should not have
• Not to be busy

```html
<!DOCTYPE html>
<html lang="en">
<head>
<meta charset="utf-8">
<title>Harwell Capital – Business Card</title>
<link rel="stylesheet" href="https://fonts.googleapis.com/css2?family=Montserrat:wght@500;600&display=swap">
<style>
  :root {
    --backdrop: #e9ecea;
    --card: #ffffff;
    --brand-green: #1fa463;
    --ink-grey: #55585a;
    --rule-grey: #d9dbdc;
  }
  html, body {
    margin: 0;
    width: 1200px;
    height: 840px;
    overflow: hidden;
    background: var(--backdrop);
  }
  .business-card {
    position: absolute;
    left: 150px;
    top: 150px;
    width: 900px;
    height: 540px;
    background: var(--card);
    box-shadow: 0 6px 24px rgba(0,0,0,0.12);
    font-family: "Montserrat", sans-serif;
  }
  .card-rules {
    position: absolute;
    inset: 0;
  }
  .brand-lockup {
    position: absolute;
    left: 0;
    right: 0;
    top: 215px;
    display: flex;
    justify-content: center;
    align-items: center;
    gap: 22px;
  }
  .brand-square {
    width: 52px;
    height: 52px;
    background: var(--ink-grey);
  }
  .brand-name {
    color: var(--brand-green);
    font-weight: 600;
    font-size: 50px;
    letter-spacing: 2px;
    text-transform: uppercase;
    line-height: 1;
  }
  .contact-block {
    position: absolute;
    left: 0;
    right: 0;
    top: 345px;
    text-align: center;
  }
  .person-line {
    margin: 0;
    color: var(--brand-green);
    font-size: 22px;
    font-weight: 500;
  }
  .person-name { font-weight: 600; }
  .details-line {
    margin: 8px 0 0;
    color: var(--ink-grey);
    font-size: 22px;
    font-weight: 500;
  }
</style>
</head>
<body>
  <div class="business-card">
    <svg class="card-rules" width="900" height="540" viewBox="0 0 900 540" aria-hidden="true">
      <g stroke="var(--rule-grey)" stroke-width="2" fill="none">
        <polyline points="40,0 40,440 0,440"/>
        <line x1="100" y1="0" x2="100" y2="430"/>
        <line x1="790" y1="0" x2="790" y2="320"/>
        <line x1="560" y1="420" x2="560" y2="540"/>
      </g>
    </svg>

    <div class="brand-lockup">
      <span class="brand-square"></span>
      <span class="brand-name">Harwell Capital</span>
    </div>

    <div class="contact-block">
      <p class="person-line"><span class="person-name">Danica Pruett</span> - Executive Assistant</p>
      <p class="details-line">P.: +64 21 547 3162 | E.: danicap@harwellcapital.co.nz</p>
    </div>
  </div>
</body>
</html>
```